Create a new website for "The Galleria at Briar Ridge"

I need a website for a shopping center in Atlanta USA. I want a classy high end look with high end motion videos (which I will provide).
The purpose of website is to attract new tenants to fill up vacant office spaces we have.
we will highlight existing cool stores and advertise that this is a cool place to start a new tenants business or office . ideally IT businesses in Harlow Springs city in Georgia state in USA

Target Market(s)

commercial office tenants

Industry/Entity Type

Real Estate

Contact Information for Business Card

classy high end design
Galleria at Briar Ridge
address:
2870 Briar Ridge Pkwy
Harlow Springs GA 30917

Logo Text

I am open. Anything that attracts new IT tech tenants to lease up shopping center/ office space

Coding

Coded - Design and coding required

Number of Pages Required

5+ page

Requirements
Must have
• easy to browse

here is a link to some photos. i will provide videos shortly

http://www.pelurano.com/2014/04/Building-Photos-3/n-7Q4hk/
Nice to have
• please look at some of mall websites i like. Moving videos and images on home page

I really like this one: https://www.plazaatcrestvane.com/

others are

https://belmorecourt.com/

https://www.visitquorrelbay.com/

```html
<!DOCTYPE html>
<html lang="en">
<head>
<meta charset="utf-8">
<title>The Galleria at Briar Ridge</title>
<link rel="stylesheet" href="https://fonts.googleapis.com/css2?family=Montserrat:wght@400;500;600;700&family=Space+Mono:wght@400;700&display=swap">
<style>
:root{
  --salmon:#f7826a;
  --salmon-soft:#f8d3c9;
  --blush:#fdf0ec;
  --ink:#2b1f1f;
  --text:#3a3a3a;
  --muted:#6b6b6b;
  --white:#ffffff;
  --line:#e6d9d5;
}
*{box-sizing:border-box;margin:0;padding:0}
html,body{width:1200px;height:3056px;overflow:hidden}
body{font-family:"Montserrat",sans-serif;color:var(--text);background:var(--white);position:relative;font-size:12px}
.abs{position:absolute}
.mono{font-family:"Space Mono",monospace}
.accent{color:var(--salmon)}

/* top bar */
.topbar{left:0;top:0;width:1200px;height:24px;background:var(--blush);font-size:10px}
.topbar .lang{left:30px;top:6px;display:flex;gap:4px;align-items:center}
.topbar .open{left:0;width:1200px;top:6px;text-align:center;color:var(--salmon);letter-spacing:.5px}
.topbar .call{right:30px;top:4px;color:var(--salmon)}
.topbar .call b{font-size:13px;font-weight:600;margin-left:4px}

/* header */
.header{left:0;top:24px;width:1200px;height:74px;background:var(--white)}
.brand{left:35px;top:22px;display:flex;align-items:center;gap:10px}
.brand-mark{width:28px;height:28px;border:4px solid var(--salmon)}
.brand-name{font-size:15px;font-weight:700;color:var(--ink);line-height:1.1}
.brand-name small{display:block;font-size:8px;font-weight:500;letter-spacing:1px;color:var(--muted)}
.nav{left:373px;top:31px;display:flex;gap:24px;font-size:11px;font-weight:500;color:var(--ink)}
.nav .active{border-bottom:1px solid var(--ink);padding-bottom:3px}
.search{left:880px;top:30px}
.tour-btn{left:1059px;top:25px;width:111px;height:26px;border-radius:13px;background:var(--ink);color:var(--white);font-size:10px;font-weight:700;display:flex;align-items:center;justify-content:center}

/* hero */
.hero{left:0;top:98px;width:1200px;height:452px;background:linear-gradient(180deg,#2f6fd0 0%,#7aaee6 35%,#f2f2f2 52%,#e9e9e9 70%,#585c63 85%,#9a9a9a 100%)}

/* intro */
.intro{left:0;top:550px;width:1200px;height:387px;background:var(--blush)}
.video-thumb{left:163px;top:615px;width:444px;height:257px;background:linear-gradient(180deg,#4a5563 0%,#c9c3b8 45%,#6e6a66 80%,#3c3c3c 100%);border:3px solid var(--salmon-soft)}
.play{left:361px;top:719px;width:50px;height:50px;border-radius:50%;background:var(--salmon);border:3px solid var(--white);display:flex;align-items:center;justify-content:center}
.intro-title{left:664px;top:603px;width:370px;font-size:25px;line-height:30px;font-weight:700;color:var(--ink)}
.intro-lead{left:664px;top:707px;width:380px;font-size:15px;line-height:21px;font-weight:500;color:var(--ink)}
.intro-body{left:664px;top:760px;width:380px;font-size:10px;line-height:18px;color:var(--muted)}
.pill{height:30px;border-radius:15px;display:flex;align-items:center;padding-left:14px;font-size:10px;font-weight:600;color:var(--white);background:var(--salmon);white-space:nowrap}
.pill .arr{margin-left:auto;width:30px;height:30px;border-radius:50%;border:2px solid var(--salmon);background:var(--white);display:flex;align-items:center;justify-content:center;flex:none}
.intro-btn{left:664px;top:845px;width:142px}

/* feature cards */
.card{top:994px;width:279px;height:351px;background:var(--ink)}
.card-photo{position:absolute;left:12px;top:12px;width:255px;height:176px}
.card-title{position:absolute;left:14px;top:202px;font-size:15px;font-weight:700;color:var(--white);letter-spacing:1.5px;white-space:nowrap}
.card-body{position:absolute;left:14px;top:230px;width:250px;font-size:10px;line-height:16px;color:#e7dcd9}
.card-link{position:absolute;left:0;bottom:0;width:279px;height:33px;background:var(--salmon);color:var(--white);font-size:11px;font-weight:500;display:flex;align-items:center;justify-content:center;gap:6px}

/* why band */
.band{left:0;top:1406px;width:1200px;height:529px;background:linear-gradient(180deg,#5d8fd6 0%,#b6c9de 30%,#d7d2c8 55%,#6d6b69 80%,#9a9591 100%)}
.why{left:161px;top:1465px;width:438px;height:411px;background:var(--white);padding:30px 44px}
.find{left:599px;top:1465px;width:440px;height:411px;background:var(--blush);padding:30px 54px}
.box-title{font-size:22px;line-height:29px;font-weight:700;color:var(--ink)}
.box-body{margin-top:14px;font-size:10px;line-height:17px;color:var(--muted)}
.ticks{list-style:none;margin-top:14px;font-size:10px;line-height:14px;color:var(--text)}
.ticks li{display:flex;gap:10px;margin-bottom:8px}
.ticks svg{flex:none;margin-top:2px}
.find-actions{display:flex;gap:10px;margin-top:26px}
.pill.dark{background:var(--ink)}
.pill.dark .arr{border-color:var(--ink)}

/* social feed */
.feed{left:0;top:1935px;width:1200px;height:453px;background:var(--blush)}
.hashtag{left:161px;top:1995px;font-size:10px;font-weight:600;color:var(--ink)}
.follow{left:161px;top:2022px;display:flex;gap:6px;align-items:center;font-size:14px;color:var(--ink);letter-spacing:1.5px}
.follow-mark{width:14px;height:14px;border:2px solid var(--ink)}
.feed-btn{left:858px;top:1998px;width:179px}
.shot{top:2068px;height:264px}
.faded{opacity:.35}
.carousel-arrow{top:2186px}

/* reviews */
.reviews-title{left:0;top:2440px;width:1200px;display:flex;justify-content:center;align-items:center;gap:8px;font-size:20px;color:var(--ink);letter-spacing:2px}
.reviews-dot{width:22px;height:22px;border-radius:50%;background:var(--salmon)}
.review{top:2526px;width:300px;display:flex;gap:14px}
.reviewer{width:80px;text-align:center;font-size:9px;color:var(--ink);white-space:nowrap}
.reviewer svg{display:block;margin:0 auto 4px}
.stars{color:var(--salmon);font-size:14px;letter-spacing:1px}
.review p{font-size:9px;line-height:14px;color:var(--muted);width:140px;margin-top:4px}

/* signup */
.signup{left:0;top:2642px;width:1200px;height:88px;background:var(--salmon-soft)}
.signup-label{left:158px;top:2672px;font-size:11px;font-weight:500;color:var(--ink)}
.signup-field{left:439px;top:2664px;width:322px;height:44px;background:var(--white);border-radius:3px;display:flex;align-items:center;justify-content:space-between;padding:0 14px;font-size:10px;color:var(--muted)}
.locate{left:940px;top:2680px;font-size:11px;font-weight:500;color:var(--ink)}

/* footer */
.footer-col{top:2770px;width:200px}
.footer-col h4{font-family:"Space Mono",monospace;font-size:14px;font-weight:400;letter-spacing:2px;color:var(--ink);margin-bottom:12px}
.footer-col li{list-style:none;font-size:11px;line-height:22px;color:var(--ink)}
.rule{left:0;top:2995px;width:1200px;height:1px;background:var(--line)}
.copyright{left:161px;top:3020px;font-size:10px;color:var(--ink)}
.socials{left:495px;top:3013px;display:flex;gap:15px}
.socials span{width:28px;height:28px;border-radius:50%;border:1px solid var(--ink);display:block}
.socials span.filled{background:var(--ink)}
</style>
</head>
<body>

<div class="abs topbar">
  <div class="abs lang"><svg width="14" height="10"><rect width="14" height="10" fill="#b22234"/><rect y="2" width="14" height="2" fill="#fff"/><rect y="6" width="14" height="2" fill="#fff"/><rect width="6" height="5" fill="#3c3b6e"/></svg><svg width="6" height="4"><path d="M0 0 L6 0 L3 4Z" fill="#333"/></svg></div>
  <div class="abs open">OPEN TODAY UNTILL 9 PM</div>
  <div class="abs call">Call Us Today: <b>123 4567 890</b></div>
</div>

<header class="abs header">
  <div class="abs brand">
    <span class="brand-mark"></span>
    <div class="brand-name">The Galleria at Briar Ridge<small>SHOPPING CENTER IN ATLANTA USA</small></div>
  </div>
  <nav class="abs nav">
    <span class="active">HOME</span><span>OFFICE SUITES</span><span>SERVICES</span><span>TENANTS</span><span>LOCATION</span><span>ABOUT US</span>
  </nav>
  <svg class="abs search" width="12" height="12" viewBox="0 0 12 12"><circle cx="5" cy="5" r="3.6" fill="none" stroke="#2b1f1f" stroke-width="1.6"/><path d="M7.7 7.7 L11 11" stroke="#2b1f1f" stroke-width="1.6"/></svg>
  <div class="abs tour-btn">REQUEST A TOUR</div>
</header>

<div class="abs hero" role="img" aria-label="Photo of the white two-storey shopping center with a car park under a blue sky"></div>

<section class="abs intro"></section>
<div class="abs video-thumb" role="img" aria-label="Video still of the center's clock tower and storefronts"></div>
<div class="abs play"><svg width="16" height="18"><path d="M2 1 L15 9 L2 17Z" fill="#fff"/></svg></div>
<h1 class="abs intro-title mono"><span class="accent">Professional, Easily Accessible</span> Office Spaces in Atlanta USA</h1>
<p class="abs intro-lead">Lorem ipsum dolor sit amet, consectetur adipiscing elit, sed do eiusmod tempor incididunt</p>
<p class="abs intro-body">Sed ut perspiciatis unde omnis iste natus error sit voluptatem accusantium doloremque laudantium, totam rem aperiam, eaque ipsa quae ab illo inventore veritatis et quasi architecto beatae vitae dicta sunt explicabo.</p>
<div class="abs pill intro-btn">Find out more<span class="arr"><svg width="12" height="10"><path d="M0 5 H10 M6 1 L10 5 L6 9" stroke="#f7826a" stroke-width="1.5" fill="none"/></svg></span></div>

<article class="abs card" style="left:161px">
  <div class="card-photo" role="img" aria-label="Photo of a sunny upper-level walkway with railings" style="background:linear-gradient(160deg,#7fa9e0 0%,#d9d4c6 45%,#b5a48d 100%)"></div>
  <h3 class="card-title mono">QUALITY SPACES</h3>
  <p class="card-body">Nemo enim ipsam voluptatem quia voluptas sit aspernatur aut odit aut fugit, sed quia consequuntur magni dolores eos qui ratione voluptatem sequi nesciunt.</p>
  <div class="card-link">View Office Suites <svg width="11" height="9"><path d="M0 4.5 H9 M5.5 1 L9 4.5 L5.5 8" stroke="#fff" stroke-width="1.3" fill="none"/></svg></div>
</article>
<article class="abs card" style="left:462px">
  <div class="card-photo" role="img" aria-label="Photo of the building from the parking lot" style="background:linear-gradient(180deg,#5f93dc 0%,#cfd6dc 45%,#8a8d91 100%)"></div>
  <h3 class="card-title mono">CONEVNIENT LOCATION</h3>
  <p class="card-body">Nemo enim ipsam voluptatem quia voluptas sit aspernatur aut odit aut fugit, sed quia consequuntur magni dolores eos qui ratione voluptatem sequi nesciunt.</p>
  <div class="card-link">View Our Loaction <svg width="11" height="9"><path d="M0 4.5 H9 M5.5 1 L9 4.5 L5.5 8" stroke="#fff" stroke-width="1.3" fill="none"/></svg></div>
</article>
<article class="abs card" style="left:762px">
  <div class="card-photo" role="img" aria-label="Photo of the building entrance and balconies" style="background:linear-gradient(180deg,#6e9ed8 0%,#e8e4dc 40%,#a8a29a 100%)"></div>
  <h3 class="card-title mono">EXCELLENT AMENITIES</h3>
  <p class="card-body">Nemo enim ipsam voluptatem quia voluptas sit aspernatur aut odit aut fugit, sed quia consequuntur magni dolores eos qui ratione voluptatem sequi nesciunt.</p>
  <div class="card-link">View Office Amenities <svg width="11" height="9"><path d="M0 4.5 H9 M5.5 1 L9 4.5 L5.5 8" stroke="#fff" stroke-width="1.3" fill="none"/></svg></div>
</article>

<div class="abs band" role="img" aria-label="Photo of storefronts and parked cars under bare trees"></div>
<section class="abs why">
  <h2 class="box-title mono"><span class="accent">Why</span> The Galleria at Briar Ridge</h2>
  <p class="box-body">Sed ut perspiciatis unde omnis iste natus error sit voluptatem accusantium doloremque laudantium, totam rem aperiam, eaque ipsa quae ab illo inventore veritatis et quasi architecto beatae vitae dicta sunt explicabo.</p>
  <ul class="ticks">
    <li><svg width="10" height="8"><path d="M1 4 L4 7 L9 1" stroke="#f7826a" stroke-width="1.6" fill="none"/></svg>Nemo enim ipsam voluptatem quia voluptas sit</li>
    <li><svg width="10" height="8"><path d="M1 4 L4 7 L9 1" stroke="#f7826a" stroke-width="1.6" fill="none"/></svg>Neque porro quisquam est, qui dolorem ipsum quiaUt</li>
    <li><svg width="10" height="8"><path d="M1 4 L4 7 L9 1" stroke="#f7826a" stroke-width="1.6" fill="none"/></svg>enim ad minima veniam, quis nostrum exercitatio-</li>
    <li><svg width="10" height="8"><path d="M1 4 L4 7 L9 1" stroke="#f7826a" stroke-width="1.6" fill="none"/></svg>nemQuis autem vel eum iure reprehenderit qui in ea voluptate velit esse quam</li>
    <li><svg width="10" height="8"><path d="M1 4 L4 7 L9 1" stroke="#f7826a" stroke-width="1.6" fill="none"/></svg>Quis autem vel eum iure reprehenderit qui in</li>
    <li><svg width="10" height="8"><path d="M1 4 L4 7 L9 1" stroke="#f7826a" stroke-width="1.6" fill="none"/></svg>Vel illum qui dolorem eum fugiat quo voluptas</li>
    <li><svg width="10" height="8"><path d="M1 4 L4 7 L9 1" stroke="#f7826a" stroke-width="1.6" fill="none"/></svg>At vero eos et accusamus et iusto odio dignissimos</li>
    <li><svg width="10" height="8"><path d="M1 4 L4 7 L9 1" stroke="#f7826a" stroke-width="1.6" fill="none"/></svg>Et harum quidem rerum facilis est et expedita</li>
  </ul>
</section>
<section class="abs find">
  <h2 class="box-title mono"><span class="accent">Find</span> Office Space Today!</h2>
  <p class="box-body">Sed ut perspiciatis unde omnis iste natus error sit voluptatem accusantium doloremque laudantium, totam rem aperiam, eaque ipsa quae ab illo inventore veritatis et quasi architecto beatae vitae dicta sunt explicabo.</p>
  <div class="find-actions">
    <div class="pill" style="width:136px">Read More<span class="arr"><svg width="12" height="10"><path d="M0 5 H10 M6 1 L10 5 L6 9" stroke="#f7826a" stroke-width="1.5" fill="none"/></svg></span></div>
    <div class="pill dark" style="width:136px">Explore Tenants<span class="arr"><svg width="12" height="10"><path d="M0 5 H10 M6 1 L10 5 L6 9" stroke="#2b1f1f" stroke-width="1.5" fill="none"/></svg></span></div>
  </div>
</section>

<section class="abs feed"></section>
<div class="abs hashtag">#yourpictorahashtag</div>
<div class="abs follow mono"><span class="follow-mark"></span>FOLLOW US ON PICTORA</div>
<div class="abs pill feed-btn">View all pictora post<span class="arr"><svg width="12" height="10"><path d="M0 5 H10 M6 1 L10 5 L6 9" stroke="#f7826a" stroke-width="1.5" fill="none"/></svg></span></div>
<div class="abs shot faded" style="left:0;width:138px;background:linear-gradient(180deg,#d8dbdf,#f1efec)" role="img" aria-label="Photo of a bright shop interior"></div>
<div class="abs shot" style="left:161px;width:277px;background:linear-gradient(180deg,#1e3d79 0%,#4a6496 40%,#c59a6a 65%,#4a4a4a 100%)" role="img" aria-label="Evening photo of lit storefronts and clock tower"></div>
<div class="abs shot" style="left:460px;width:277px;background:linear-gradient(180deg,#7fa8de 0%,#c8c8c4 45%,#9c6a52 80%,#7a5646 100%)" role="img" aria-label="Photo of the entrance sign with flower beds"></div>
<div class="abs shot" style="left:760px;width:277px;background:linear-gradient(180deg,#a9c6ea 0%,#e8e6e0 50%,#8d8f93 85%,#a6a6a6 100%)" role="img" aria-label="Photo of the building with a cupola and parking"></div>
<div class="abs shot faded" style="left:1061px;width:139px;background:linear-gradient(180deg,#c9d9ef,#e9e3dd)" role="img" aria-label="Photo of storefronts"></div>
<svg class="abs carousel-arrow" style="left:52px" width="14" height="24"><path d="M12 2 L3 12 L12 22" stroke="#fff" stroke-width="2.5" fill="none"/></svg>
<svg class="abs carousel-arrow" style="left:1130px" width="14" height="24"><path d="M2 2 L11 12 L2 22" stroke="#fff" stroke-width="2.5" fill="none"/></svg>

<h2 class="abs reviews-title mono"><span class="reviews-dot"></span>REVIEWS</h2>
<div class="abs review" style="left:150px">
  <div class="reviewer"><svg width="28" height="28"><circle cx="14" cy="9" r="7" fill="#c8c8c8"/><path d="M1 28 Q14 12 27 28Z" fill="#c8c8c8"/></svg>Customer Name</div>
  <div><div class="stars">★★★★★</div><p>At vero eos et accusamus et iusto odio dignissimos ducmus qui blanditiis</p></div>
</div>
<div class="abs review" style="left:490px">
  <div class="reviewer"><svg width="28" height="28"><circle cx="14" cy="9" r="7" fill="#c8c8c8"/><path d="M1 28 Q14 12 27 28Z" fill="#c8c8c8"/></svg>Customer Name</div>
  <div><div class="stars">★★★★★</div><p>At vero eos et accusamus et iusto odio dignissimos</p></div>
</div>
<div class="abs review" style="left:796px">
  <div class="reviewer"><svg width="28" height="28"><circle cx="14" cy="9" r="7" fill="#c8c8c8"/><path d="M1 28 Q14 12 27 28Z" fill="#c8c8c8"/></svg>Customer Name</div>
  <div><div class="stars">★★★★★</div><p>At vero eos et accusamus et iusto odio dignissimos ducmus qui blanditiis</p></div>
</div>

<section class="abs signup"></section>
<div class="abs signup-label">Signup for news, sales or catalog</div>
<div class="abs signup-field">Enter your email address<svg width="14" height="10"><rect x="0.7" y="0.7" width="12.6" height="8.6" fill="none" stroke="#f7826a" stroke-width="1.3"/><path d="M1 1 L7 6 L13 1" stroke="#f7826a" stroke-width="1.3" fill="none"/></svg></div>
<div class="abs locate">FIND A LOCATION</div>

<div class="abs footer-col" style="left:161px"><h4>ADDRESS</h4><ul><li>2870 Briar Ridge Pkwy</li><li>Harlow Springs</li><li>GA 30917</li><li>GET DIRECTIONS</li></ul></div>
<div class="abs footer-col" style="left:385px"><h4>POPULAR</h4><ul><li>Visit Us</li><li>Reviews</li><li>FAQ</li><li>Terms</li><li>Privacy Policy</li></ul></div>
<div class="abs footer-col" style="left:609px"><h4>QUICK LINKS</h4><ul><li>Home</li><li>Office Suites</li><li>Services</li><li>Tenants</li><li>Location</li><li>About Us</li></ul></div>
<div class="abs footer-col" style="left:835px"><h4>GET HELP</h4><ul><li>Help &amp; FAQs</li><li>Email Us</li><li>(123) 456 7890</li></ul></div>

<div class="abs rule"></div>
<div class="abs copyright">© <span class="accent">The Galleria at Briar Ridge</span> 2020 All rights reserved</div>
<div class="abs socials"><span class="filled"></span><span></span><span></span><span></span><span></span></div>

</body>
</html>
```